A Label for an ECO Friendly Spirit Company

Design a label which can be used for vodka and gin (London Dry Gin). It should be Square type Like the Shape File you see in the uploads. VORK means Local Eco friendly Authentic and Fair. We want a cool and slim label that calls for eco-friendly. We want to use it for our premium
Vodka and our London Dry Gin. Please use the logo and design it in Square Type.

40%vol, 700ml

Target Market(s)

spirits and events

Industry/Entity Type

SPIRITS

Colors
00AB8E
00BBA5
67D7C9
C6EFE9
E9F9F6
59FF00
82FF00
B8FF75
E3FFCB
F4FFEA

Requirements
Must have
• Logo from VORK, Squaee Shape

```html
<!DOCTYPE html>
<html lang="en">
<head>
<meta charset="utf-8">
<title>VORK Spirits – Square Labels</title>
<link rel="stylesheet" href="https://fonts.googleapis.com/css2?family=Oswald:wght@400;500&display=swap">
<style>
  :root {
    --paper: #ffffff;
    --board: #ede7e4;
    --teal: #24ad92;
    --green: #8cc63f;
    --white: #ffffff;
    --leaf-deep: #00ab8e;
    --leaf-mint: #1ef2a6;
    --leaf-coral: #f9895f;
    --leaf-red: #f2405c;
    --leaf-yellow: #e9f24a;
  }
  html, body {
    margin: 0;
    padding: 0;
    width: 1200px;
    height: 723px;
    overflow: hidden;
    background: var(--paper);
  }
  .label-sheet {
    display: block;
    width: 1200px;
    height: 723px;
  }
  .label-text {
    font-family: "Oswald", "Arial Narrow", sans-serif;
    text-anchor: middle;
  }
  .brand-name { font-weight: 500; font-size: 112px; fill: var(--teal); letter-spacing: 6px; }
  .style-name { font-weight: 500; font-size: 112px; fill: var(--white); }
  .spec { font-weight: 400; font-size: 40px; fill: var(--teal); }
  .spirit-name { font-weight: 500; font-size: 58px; fill: var(--teal); letter-spacing: 2px; }
  .board { fill: var(--board); }
  .frame-outer { fill: none; stroke: var(--teal); stroke-width: 9; }
  .frame-inner { fill: none; stroke: var(--green); stroke-width: 5; }
  .brand-square { fill: var(--green); }
  .ribbon-gin { fill: var(--teal); }
  .ribbon-vodka { fill: var(--green); }
  .ribbon-stitch { fill: none; stroke: var(--white); stroke-width: 3; stroke-dasharray: 10 7; }
  .foliage { fill: url(#foliage-tones); }
</style>
</head>
<body>
<svg class="label-sheet" viewBox="0 0 2460 1482" xmlns="http://www.w3.org/2000/svg">
  <defs>
    <clipPath id="label-shape">
      <polygon points="674,215 1200,742 674,1268 148,742"/>
    </clipPath>
    <linearGradient id="foliage-tones" x1="0" y1="0" x2="1" y2="1">
      <stop offset="0" stop-color="var(--leaf-deep)"/>
      <stop offset="0.35" stop-color="var(--leaf-mint)"/>
      <stop offset="0.6" stop-color="var(--leaf-coral)"/>
      <stop offset="0.8" stop-color="var(--leaf-yellow)"/>
      <stop offset="1" stop-color="var(--leaf-red)"/>
    </linearGradient>
    <g id="label-base">
      <polygon class="board" points="674,215 1200,742 674,1268 148,742"/>
      <polygon class="frame-outer" points="674,262 1155,742 674,1223 193,742"/>
      <polygon class="frame-inner" points="674,284 1133,742 674,1201 215,742"/>
      <rect class="brand-square" x="600" y="400" width="152" height="156" rx="16"/>
      <text class="label-text brand-name" x="674" y="642">VORK</text>
      <text class="label-text spec" x="315" y="730">700</text>
      <text class="label-text spec" x="315" y="770">ML</text>
      <text class="label-text spec" x="1028" y="730">40%</text>
      <text class="label-text spec" x="1028" y="770">VOL</text>
      <g clip-path="url(#label-shape)">
        <path class="foliage" role="img" aria-label="Colourful tropical leaves illustration"
          d="M306,900 L330,890 L480,826 L560,838 L620,960 L700,940 L760,950 L850,860 L975,930 L990,960 L1200,742 L674,1268 L148,742 Z"/>
      </g>
    </g>
    <g id="ribbon-stitch-line">
      <path class="ribbon-stitch" d="M368,678 L985,682 L918,740 L985,798 L362,800 L432,740 Z"/>
    </g>
  </defs>

  <g class="label label-gin">
    <use href="#label-base"/>
    <path class="ribbon-gin" d="M345,666 L1003,670 L930,740 L1003,808 L343,810 L418,740 Z"/>
    <use href="#ribbon-stitch-line"/>
    <text class="label-text style-name" x="684" y="780" textLength="470" lengthAdjust="spacingAndGlyphs">LONDON DRY</text>
    <text class="label-text spirit-name" x="674" y="922">GIN</text>
  </g>

  <g class="label label-vodka" transform="translate(1116 0)">
    <use href="#label-base"/>
    <path class="ribbon-vodka" d="M345,666 L1003,670 L930,740 L1003,808 L343,810 L418,740 Z"/>
    <use href="#ribbon-stitch-line"/>
    <text class="label-text style-name" x="684" y="780" textLength="470" lengthAdjust="spacingAndGlyphs">LONDON DRY</text>
    <text class="label-text spirit-name" x="674" y="918">VODKA</text>
  </g>
</svg>
</body>
</html>
```